Quorvex clinic business card - double sided for young clinic

I require business cards for my aesthetic clinic specialising in the below treatments. I would like the cards to be modern as my clinic base are young 22-35 years old. I require my logo on it and would like the edges to be rounded.

I have an aesthetic clinic specialising in :
Quorvex
Lip Enhancement
Chemical Peels
Facial Fillers
Non Surgical Face Lift

I would the cards to have the following information on them:
My logo - (in grey/silver)
address
Phone number
services

Colours :
White/grey/silver and red

a nice image on there, perhaps a set of lips as this is a main service i deliver

Company Name: PDA Address: 52 Farrowmere Road, 4 Brackwell High Street, KT9 4WQ Phone: 0208 794 2160 Website: www.penningtondoweaesthetics.co.uk

Target Market(s)

clinics 22-45 years old mainly female

Industry/Entity Type

Business

Contact Information for Business Card

as above

Requirements
Must have
• logo
• Address
• Email
• Phone number
• Services i offer
Nice to have
• images

```html
<!DOCTYPE html>
<html lang="en">
<head>
<meta charset="utf-8">
<title>PDA – Pennington Dowe Aesthetics business card</title>
<link href="https://fonts.googleapis.com/css2?family=Libre+Baskerville:wght@400;700&display=swap" rel="stylesheet">
<style>
  :root {
    --page-bg: #e9e6e2;
    --card-white: #fbfbfb;
    --band-dark: #6f6f70;
    --band-light: #b9b9bb;
    --ink-grey: #6a6a6b;
    --ink-light: #f4f4f4;
    --ink-muted: #5c5c5e;
    --lip-deep: #d98e8c;
    --lip-soft: #e9b3a6;
    --skin: #d7ab95;
    --skin-light: #e7c6b3;
    --badge-ink: #6b3b34;
  }
  * { box-sizing: border-box; margin: 0; padding: 0; }
  html, body { width: 1200px; height: 1023px; overflow: hidden; }
  body {
    background: var(--page-bg);
    font-family: "Libre Baskerville", Georgia, serif;
    position: relative;
  }
  .card {
    position: absolute;
    width: 540px;
    height: 348px;
    border-radius: 26px;
    overflow: hidden;
    box-shadow: 0 10px 28px rgba(0,0,0,0.18);
  }
  /* Info side */
  .card--info { left: 70px; top: 110px; background: var(--card-white); display: flex; flex-direction: column; }
  .info__brand {
    height: 156px;
    display: flex; flex-direction: column; align-items: center; justify-content: center;
    gap: 10px;
  }
  .brand-mark {
    display: flex; align-items: center; gap: 12px;
  }
  .brand-mark__dot {
    width: 18px; height: 18px; border-radius: 50%; background: var(--ink-grey);
  }
  .brand-mark__name {
    font-size: 30px; letter-spacing: 6px; color: var(--ink-grey);
  }
  .brand-name { text-align: center; color: var(--ink-grey); line-height: 1.1; }
  .brand-name__top { font-size: 13px; letter-spacing: 4px; }
  .brand-name__main { font-size: 24px; letter-spacing: 5px; }
  .info__contact {
    height: 116px; background: var(--band-dark); color: var(--ink-light);
    display: flex; flex-direction: column; align-items: center; justify-content: center;
    font-size: 12.5px; line-height: 1.65; letter-spacing: 0.5px; text-align: center;
  }
  .info__services {
    flex: 1; background: var(--band-light); color: var(--ink-muted);
    display: flex; flex-direction: column; align-items: center; justify-content: center;
    font-size: 12.5px; line-height: 1.6; letter-spacing: 0.5px; text-align: center;
  }
  /* Image side */
  .card--image { left: 590px; top: 560px; }
  .lips-photo {
    position: absolute; inset: 0;
    background:
      radial-gradient(ellipse 42% 26% at 50% 52%, var(--lip-deep) 0%, var(--lip-soft) 60%, rgba(233,179,166,0) 100%),
      linear-gradient(160deg, var(--skin-light), var(--skin));
  }
  .image__brand {
    position: absolute; inset: 0;
    display: flex; align-items: center; justify-content: center; gap: 22px;
  }
  .image__badge {
    width: 120px; height: 120px; border-radius: 50%; background: var(--card-white);
    display: flex; align-items: center; justify-content: center;
    font-size: 30px; letter-spacing: 5px; color: var(--badge-ink);
  }
  .image__name { color: var(--ink-light); line-height: 1.1; }
  .image__name-top { font-size: 14px; letter-spacing: 4px; }
  .image__name-main { font-size: 27px; letter-spacing: 5px; }
</style>
</head>
<body>
  <section class="card card--info" aria-label="Business card, contact side">
    <div class="info__brand">
      <div class="brand-mark">
        <span class="brand-mark__dot"></span>
        <span class="brand-mark__name">PDA</span>
      </div>
      <div class="brand-name">
        <div class="brand-name__top">PENNINGTON DOWE</div>
        <div class="brand-name__main">AESTHETICS</div>
      </div>
    </div>
    <div class="info__contact">
      <p class="contact__phone">0208 794 2160</p>
      <p class="contact__email">info@penningtondoweaesthetics.co.uk</p>
      <p class="contact__web">www.penningtondoweaesthetics.co.uk</p>
      <p class="contact__address">52 Farrowmere Road, 4 Brackwell High Street, KT9 4WQ</p>
    </div>
    <div class="info__services">
      <p>Quorvex | Lip Enhancement | Chemical Peels</p>
      <p>Facial Fillers | Non Surgical Face Lift</p>
    </div>
  </section>

  <section class="card card--image" aria-label="Business card, image side">
    <div class="lips-photo" role="img" aria-label="Close-up photograph of soft pink lips"></div>
    <div class="image__brand">
      <div class="image__badge">PDA</div>
      <div class="image__name">
        <div class="image__name-top">PENNINGTON DOWE</div>
        <div class="image__name-main">AESTHETICS</div>
      </div>
    </div>
  </section>
</body>
</html>
```